Design an investor pitch deck for Brindlework.io

We delivered a killer investor pitch to a group of investors last week and have been asked for a deck. we need to follow up with a killer printed version. I have produced the attached file using free images from fotovane. Feel free to change the imagery as you see fit. Check out brindlework.io to get a feel for the look and feel we have right now.

Target Market(s)

Investors

Industry/Entity Type

Software

Font styles to use
Sans Serif
Other font styles liked:
• Helvetica

Requirements
Must have
• A new version of each of the pages in the example documents. Needs to be slick and professional
Nice to have
• Other layouts in case I add further slides
Should not have
• Childish or dated shapes or designs

```html
<!DOCTYPE html>
<html lang="en">
<head>
<meta charset="utf-8">
<title>Brindlework — Investor Deck Layouts</title>
<link rel="stylesheet" href="https://fonts.googleapis.com/css2?family=Roboto:wght@300;400;500;700&display=swap">
<style>
:root{
  --grey:#b5b5b7;
  --grey-dark:#8e8e90;
  --ink:#2b2b2b;
  --muted:#6b6b6b;
  --navy:#1f4f9c;
  --navy-deep:#0f2347;
  --orange:#f6a531;
  --charcoal:#3c3c3c;
  --white:#ffffff;
  --line:#d6d6d6;
}
*{box-sizing:border-box;margin:0;padding:0}
html,body{width:1200px;height:2767px;overflow:hidden;background:var(--white)}
body{position:relative;font-family:"Roboto",Helvetica,Arial,sans-serif;color:var(--ink)}
.slide{position:absolute;background:var(--white);overflow:hidden}
.slide.framed{box-shadow:0 0 0 1px #ececec}
.bar{position:absolute;left:0;right:0;top:0;height:44px;background:var(--grey);display:flex;align-items:center;justify-content:center;color:var(--white);font-size:21px;font-weight:400}
.bar .dot{position:absolute;left:12px;top:8px;width:28px;height:28px;border-radius:50%;border:3px solid var(--white)}
.photo{position:absolute}
.city{background:linear-gradient(135deg,#0b1830 0%,#163a74 40%,#2a6bb8 60%,#0d1f3d 100%)}
.hero-band{position:absolute;background:var(--grey);color:var(--white)}
.brand{font-weight:500}
.small{font-size:9px;line-height:1.35;color:var(--muted)}
.tag{font-weight:300}
.name{font-weight:500;font-size:11px}
.circle-node{position:absolute;border-radius:50%;border:2px solid var(--orange);display:flex;align-items:center;justify-content:center;text-align:center;color:var(--muted);font-size:13px;line-height:1.25}
.partner{font-size:11px;font-weight:700;color:var(--ink)}
.pill{position:absolute;left:60px;height:26px;background:var(--grey);color:var(--white);font-size:13px;display:flex;align-items:center;padding-left:10px}
.icon{position:absolute;width:22px;height:22px;border-radius:50%;border:1.5px solid var(--grey-dark)}
.tick li{list-style:none;position:relative;padding-left:16px;margin-bottom:11px;font-size:12px;color:var(--muted);line-height:1.3}
.tick li::before{content:"";position:absolute;left:0;top:3px;width:6px;height:3px;border-left:1.5px solid var(--navy);border-bottom:1.5px solid var(--navy);transform:rotate(-45deg)}
.box-label{position:absolute;font-size:11px;color:var(--muted);line-height:1.3}
</style>
</head>
<body>

<!-- Row 1 -->
<div class="photo" style="left:0;top:0;width:268px;height:292px;background:linear-gradient(160deg,#d9d4cf,#8c8680 55%,#4b4744)" role="img" aria-label="Photo of a person checking a wristwatch while waiting"></div>
<section class="slide" style="left:268px;top:0;width:258px;height:292px">
  <div style="position:absolute;left:62px;top:42px;width:28px;height:28px;border-radius:50%;border:3px solid var(--navy)"></div>
  <div class="brand" style="position:absolute;left:36px;top:96px;font-size:34px;color:var(--navy-deep)">Brindlework</div>
  <div class="tag" style="position:absolute;left:38px;top:140px;font-size:15px;color:var(--muted);line-height:1.25">Waiting sucks. Brindlework<br>makes it better.</div>
  <div style="position:absolute;right:14px;top:236px;text-align:right;font-size:9px;color:var(--muted);line-height:1.3">Owen Harlow<br>Founder &amp; Head of Engineering<br>owen@brindlework.io</div>
</section>
<section class="slide" style="left:526px;top:0;width:521px;height:292px">
  <div class="photo city" style="left:0;top:0;width:521px;height:292px" role="img" aria-label="Night city with glowing data lines and delivery icons"></div>
  <div class="hero-band" style="left:0;top:0;width:521px;height:100px">
    <div style="position:absolute;left:14px;top:14px;width:30px;height:30px;border-radius:50%;border:3px solid var(--white)"></div>
    <div class="brand" style="position:absolute;left:60px;top:12px;font-size:32px">Brindlework</div>
    <div class="tag" style="position:absolute;left:62px;top:56px;font-size:16px">Waiting sucks. Brindlework makes it better.</div>
  </div>
  <div style="position:absolute;right:14px;bottom:12px;text-align:right;font-size:9px;color:#dbe4f2;line-height:1.3">Owen Harlow<br>Founder &amp; Head of Engineering<br>owen@brindlework.io</div>
</section>

<!-- Row 2 -->
<section class="slide" style="left:6px;top:318px;width:524px;height:292px">
  <div class="photo city" style="left:0;top:0;width:524px;height:292px" role="img" aria-label="Night city with glowing data lines and delivery icons"></div>
  <div class="hero-band" style="left:0;top:0;width:524px;height:100px">
    <div style="position:absolute;left:14px;top:16px;width:30px;height:30px;border-radius:50%;border:3px solid var(--white)"></div>
    <div class="brand" style="position:absolute;left:60px;top:14px;font-size:32px">Brindlework</div>
    <div class="tag" style="position:absolute;left:62px;top:58px;font-size:16px">Waiting sucks. Brindlework makes it better.</div>
  </div>
  <div style="position:absolute;left:0;right:0;bottom:0;height:30px;background:var(--navy)"></div>
  <div style="position:absolute;right:14px;bottom:6px;text-align:right;font-size:9px;color:var(--white);line-height:1.3">Owen Harlow<br>Founder &amp; Head of Engineering · owen@brindlework.io</div>
</section>
<section class="slide" style="left:541px;top:318px;width:523px;height:292px">
  <div class="photo city" style="left:0;top:0;width:523px;height:292px" role="img" aria-label="Night city with glowing data lines and delivery icons"></div>
  <div style="position:absolute;left:0;top:168px;width:158px;height:124px;background:var(--grey)">
    <div style="position:absolute;left:44px;top:14px;width:44px;height:44px;border-radius:50%;border:3px solid var(--white)"></div>
    <div style="position:absolute;left:8px;top:76px;font-size:9px;color:var(--white);line-height:1.3">Owen Harlow<br>Founder &amp; Head of Engineering<br>owen@brindlework.io</div>
  </div>
  <div style="position:absolute;left:158px;top:168px;right:0;height:124px;background:var(--navy);color:var(--white)">
    <div class="brand" style="position:absolute;left:22px;top:22px;font-size:32px">Brindlework</div>
    <div class="tag" style="position:absolute;left:22px;top:66px;font-size:15px">Waiting Sucks. Brindlework Makes It Better.</div>
  </div>
</section>

<!-- Row 3 -->
<section class="slide" style="left:6px;top:628px;width:517px;height:286px">
  <div class="bar"><span class="dot"></span>The Big Idea in 125 words</div>
  <div style="position:absolute;left:20px;right:20px;top:60px;text-align:center;font-size:17px;color:var(--ink);font-weight:300;line-height:1.3">Waiting sucks. Live tracking makes waiting for deliveries<br>and services less painful. Brindlework makes it easy.</div>
  <div class="icon" style="left:76px;top:118px"></div>
  <div class="icon" style="left:240px;top:118px"></div>
  <div class="icon" style="left:394px;top:118px"></div>
  <div class="small" style="position:absolute;left:10px;top:152px;width:150px">You could track your pizza in real time since 2015. Now businesses of all sizes expect it, yet building live tracking is unnecessarily hard and costly.</div>
  <div class="small" style="position:absolute;left:178px;top:170px;width:150px">Why now? Everyone expects live tracking, yet legacy processes, complex integrations and multiple providers leave a poor, disjointed customer experience.</div>
  <div class="small" style="position:absolute;left:346px;top:152px;width:160px">Brindlework is the simplest way to give customers live tracking, helping drivers and developers deliver great service and capture honest feedback.</div>
</section>
<section class="slide" style="left:554px;top:624px;width:510px;height:290px">
  <div class="photo" style="left:0;top:0;width:242px;height:290px;background:linear-gradient(170deg,#5b5a57,#2d2c2b 60%,#1a1a1a)" role="img" aria-label="Dim street scene photo behind the headline"></div>
  <div style="position:absolute;left:24px;top:52px;font-size:30px;color:var(--white);line-height:1.15">The Big Idea<br>in 125 words</div>
  <div style="position:absolute;left:24px;top:140px;width:200px;font-size:16px;color:#e8e8e8;font-weight:300;line-height:1.35">Waiting sucks. Live tracking makes waiting for deliveries and services less painful. Brindlework makes it easy.</div>
  <div class="icon" style="left:252px;top:16px"></div>
  <div class="small" style="position:absolute;left:284px;top:12px;width:216px">You could track your pizza in real time since 2015. Now businesses of all sizes expect it, yet building live tracking is unnecessarily hard and costly.</div>
  <div class="icon" style="left:252px;top:100px"></div>
  <div class="small" style="position:absolute;left:284px;top:96px;width:216px">Why now? Everyone expects live tracking, yet legacy processes, complex integrations and multiple providers leave a poor, disjointed experience.</div>
  <div class="icon" style="left:252px;top:184px"></div>
  <div class="small" style="position:absolute;left:284px;top:180px;width:216px">Brindlework is the simplest way to give customers live tracking, helping drivers and developers deliver great service and capture honest feedback.</div>
  <div style="position:absolute;right:12px;bottom:10px;width:16px;height:16px;border-radius:50%;border:2px solid var(--navy)"></div>
</section>

<!-- Row 4 -->
<section class="slide" style="left:6px;top:932px;width:517px;height:286px">
  <div class="bar"><span class="dot"></span>Why Now?</div>
  <div class="circle-node" style="left:64px;top:72px;width:118px;height:118px">Simple<br>Global<br>Deployment</div>
  <div class="circle-node" style="left:200px;top:72px;width:118px;height:118px">Success of<br>best in class<br>integration</div>
  <div class="circle-node" style="left:336px;top:72px;width:118px;height:118px">Shifting<br>Customer<br>Expectation</div>
  <div class="partner" style="position:absolute;left:86px;top:198px">Nimbus Cloud</div>
  <div class="partner" style="position:absolute;left:100px;top:222px">Callwire</div>
  <div class="partner" style="position:absolute;left:240px;top:200px">Paylane</div>
  <div class="partner" style="position:absolute;left:212px;top:226px">Ledgerly</div>
  <div class="partner" style="position:absolute;left:276px;top:226px">Chatloom</div>
  <div class="partner" style="position:absolute;left:364px;top:200px">Nimbus</div>
  <div class="partner" style="position:absolute;left:420px;top:200px">Crustco</div>
  <div class="partner" style="position:absolute;left:364px;top:230px">Ridebite</div>
  <div class="partner" style="position:absolute;left:428px;top:230px">Rydo</div>
</section>
<section class="slide" style="left:550px;top:932px;width:517px;height:286px">
  <div class="bar" style="left:170px"><span class="dot"></span>Why Now?</div>
  <div class="photo" style="left:0;top:0;width:170px;height:286px;background:linear-gradient(180deg,#eef1f6,#cfd7e4)" role="img" aria-label="Screenshot of a live tracking map dashboard"></div>
  <div class="icon" style="left:186px;top:64px;width:30px;height:30px"></div>
  <div style="position:absolute;left:232px;top:64px;font-size:12px;color:var(--muted);line-height:1.3">Simple Global<br>Deployment</div>
  <div class="partner" style="position:absolute;left:360px;top:70px">Nimbus Cloud · Callwire</div>
  <div class="icon" style="left:186px;top:138px;width:30px;height:30px"></div>
  <div style="position:absolute;left:232px;top:138px;font-size:12px;color:var(--muted);line-height:1.3">Success of best-in-<br>class integration</div>
  <div class="partner" style="position:absolute;left:380px;top:134px">Ledgerly Chatloom</div>
  <div class="partner" style="position:absolute;left:434px;top:152px">Paylane</div>
  <div class="icon" style="left:186px;top:212px;width:30px;height:30px"></div>
  <div style="position:absolute;left:232px;top:212px;font-size:12px;color:var(--muted);line-height:1.3">Shifting Customer<br>Expectation</div>
  <div class="partner" style="position:absolute;left:390px;top:206px">Nimbus Crustco</div>
  <div class="partner" style="position:absolute;left:390px;top:230px">Ridebite Rydo</div>
</section>

<!-- Row 5 -->
<section class="slide" style="left:6px;top:1237px;width:517px;height:286px">
  <div class="bar"><span class="dot"></span>Why Now?</div>
  <svg style="position:absolute;left:0;top:0" width="517" height="286" aria-hidden="true">
    <circle cx="258" cy="162" r="72" fill="#cfcfcf"/>
    <circle cx="258" cy="162" r="34" fill="#fff"/>
    <circle cx="258" cy="92" r="20" fill="#fff" stroke="#f6a531" stroke-width="2"/>
    <circle cx="192" cy="196" r="20" fill="#fff" stroke="#f6a531" stroke-width="2"/>
    <circle cx="324" cy="196" r="20" fill="#fff" stroke="#f6a531" stroke-width="2"/>
    <circle cx="258" cy="162" r="10" fill="none" stroke="#3c3c3c" stroke-width="2"/>
  </svg>
  <div style="position:absolute;left:196px;top:60px;font-size:12px;color:var(--muted)">Simple Global Deployment</div>
  <div class="partner" style="position:absolute;left:372px;top:60px">Nimbus Callwire</div>
  <div style="position:absolute;left:40px;top:170px;font-size:12px;color:var(--muted);line-height:1.3;text-align:center">Success of best in<br>class integration</div>
  <div class="partner" style="position:absolute;left:40px;top:212px">Ledgerly Chatloom Paylane</div>
  <div style="position:absolute;left:350px;top:140px;font-size:12px;color:var(--muted);line-height:1.3">Shifting Customer<br>Expectation</div>
  <div class="partner" style="position:absolute;left:350px;top:186px">Nimbus Crustco</div>
  <div class="partner" style="position:absolute;left:350px;top:210px">Ridebite Rydo</div>
</section>
<section class="slide" style="left:550px;top:1237px;width:517px;height:286px">
  <div class="bar"><span class="dot"></span>The Solution</div>
  <div class="icon" style="left:60px;top:108px;border-color:var(--orange)"></div>
  <div class="box-label" style="left:26px;top:140px;width:94px;font-size:9px">Integrates with common couriers, apps and automation tools</div>
  <div style="position:absolute;left:150px;top:120px;font-size:11px;color:var(--grey-dark)">›</div>
  <div class="icon" style="left:210px;top:104px;border-color:var(--orange)"></div>
  <div class="box-label" style="left:176px;top:136px;width:100px;font-size:9px">Simple setup that keeps your customers updated in real time</div>
  <div style="position:absolute;left:300px;top:110px;font-size:11px;color:var(--grey-dark)">›</div>
  <div class="icon" style="left:330px;top:62px;border-color:var(--orange)"></div>
  <div class="box-label" style="left:362px;top:62px;width:140px;font-size:9px">A clean live view that lets drivers deliver on time, every time</div>
  <div class="icon" style="left:330px;top:130px;border-color:var(--orange)"></div>
  <div class="box-label" style="left:362px;top:130px;width:140px;font-size:9px">A clear dashboard with live SMS and honest feedback</div>
</section>

<!-- Row 6 -->
<section class="slide" style="left:6px;top:1547px;width:517px;height:281px">
  <div class="bar"><span class="dot"></span>Market Size</div>
  <div class="small" style="position:absolute;left:22px;top:70px;width:170px;font-size:9px">1&nbsp;&nbsp; Global on-demand delivery market projected to grow steadily to 2021.</div>
  <div class="small" style="position:absolute;left:22px;top:120px;width:170px;font-size:9px">2&nbsp;&nbsp; Global e-commerce deliveries forecast to rise strongly this decade.</div>
  <div class="small" style="position:absolute;left:22px;top:168px;width:170px;font-size:9px">3&nbsp;&nbsp; Based on courier volumes, a market of billions of tracked jobs a year.</div>
  <svg style="position:absolute;left:205px;top:66px" width="300" height="190" aria-label="Bar chart of market size by segment">
    <line x1="10" y1="160" x2="290" y2="160" stroke="#bbb"/>
    <g fill="#f6a531">
      <rect x="14" y="30" width="16" height="130"/><rect x="38" y="50" width="16" height="110"/>
      <rect x="62" y="64" width="16" height="96"/><rect x="86" y="80" width="16" height="80"/>
      <rect x="110" y="96" width="16" height="64"/><rect x="134" y="110" width="16" height="50"/>
      <rect x="158" y="124" width="16" height="36"/><rect x="182" y="134" width="16" height="26"/>
      <rect x="206" y="142" width="16" height="18"/><rect x="230" y="148" width="16" height="12"/>
      <rect x="254" y="152" width="16" height="8"/>
    </g>
    <g fill="#555">
      <rect x="14" y="16" width="16" height="30"/><rect x="38" y="38" width="16" height="22"/>
      <rect x="62" y="54" width="16" height="16"/><rect x="86" y="72" width="16" height="12"/>
      <rect x="110" y="90" width="16" height="8"/><rect x="134" y="106" width="16" height="6"/>
      <rect x="158" y="120" width="16" height="5"/>
    </g>
  </svg>
</section>
<section class="slide" style="left:532px;top:1547px;width:520px;height:281px">
  <div class="bar"><span class="dot"></span>Business Model</div>
  <div class="icon" style="left:24px;top:74px;width:20px;height:20px;border-radius:3px"></div>
  <div class="pill" style="top:72px;width:210px">Transactional pricing</div>
  <div class="icon" style="left:24px;top:124px;width:20px;height:20px"></div>
  <div class="pill" style="top:122px;width:250px">Brindlework: 19c per task (USD)</div>
  <div class="icon" style="left:24px;top:174px;width:20px;height:20px"></div>
  <div class="pill" style="top:172px;width:300px">Credit and top-up like a pre-paid phone card</div>
  <div class="icon" style="left:24px;top:224px;width:20px;height:20px"></div>
  <div class="pill" style="top:222px;width:320px">Bonus credit for higher top-up amounts</div>
</section>

<!-- Row 7 -->
<section class="slide" style="left:6px;top:1852px;width:517px;height:290px">
  <div class="bar"><span class="dot"></span>Go To Market</div>
  <div class="small" style="position:absolute;left:20px;top:56px;width:480px;font-size:8.5px">Brindlework already serves paying customers in several countries. Early traction came from developers finding the API on their own; a simple self-serve signup turns this interest into revenue with little sales effort.</div>
  <svg style="position:absolute;left:20px;top:110px" width="200" height="170" aria-hidden="true">
    <circle cx="60" cy="80" r="78" fill="#f6a531"/>
    <circle cx="72" cy="80" r="54" fill="#f9c57a"/>
    <circle cx="84" cy="80" r="30" fill="#fde3bd"/>
  </svg>
  <div class="small" style="position:absolute;left:40px;top:160px;width:70px;color:var(--white);font-size:9px">Our Go-to-market plan is built around a repeatable sales process</div>
  <div class="small" style="position:absolute;left:260px;top:124px;width:240px;font-size:8.5px">Developers discover the platform through search and communities, trial it for free and convert to paid plans as volumes grow.</div>
  <div class="small" style="position:absolute;left:260px;top:180px;width:240px;font-size:8.5px">Partnerships with couriers and platforms widen reach and bring in teams that already need live tracking today.</div>
  <div class="small" style="position:absolute;left:260px;top:230px;width:240px;font-size:8.5px">Customer success turns early users into advocates across key regions.</div>
</section>
<section class="slide" style="left:556px;top:1852px;width:512px;height:290px">
  <div style="position:absolute;left:0;top:0;width:170px;height:290px;background:var(--charcoal)">
    <div style="position:absolute;left:56px;top:70px;width:56px;height:56px;border-radius:50%;border:4px solid var(--white)"></div>
    <div style="position:absolute;left:0;right:0;top:150px;text-align:center;color:var(--white);font-size:22px">Our Team</div>
  </div>
  <ul class="tick" style="position:absolute;left:192px;top:60px;width:300px">
    <li>Unique access to technical talent pipeline from our partnership with and colocation at Coastline University</li>
    <li>Battle hardened from bootstrapping for 3 years</li>
    <li>All key players have skin in the game</li>
    <li>Founder &amp; board's commercial experience</li>
  </ul>
</section>

<!-- Row 8 -->
<section class="slide" style="left:6px;top:2160px;width:517px;height:262px">
  <div class="bar"><span class="dot"></span>Finance &amp; Opportunity</div>
  <div style="position:absolute;left:50px;top:86px;font-size:14px;color:var(--ink)">2016</div>
  <div style="position:absolute;left:236px;top:86px;font-size:14px;color:var(--ink)">Now</div>
  <div style="position:absolute;left:406px;top:86px;font-size:14px;color:var(--ink)">6-8 months</div>
  <svg style="position:absolute;left:0;top:130px" width="517" height="40" aria-hidden="true">
    <line x1="60" y1="20" x2="460" y2="20" stroke="#d0d0d0" stroke-width="2" stroke-dasharray="3 4"/>
    <rect x="40" y="14" width="70" height="12" fill="#3c3c3c"/>
    <rect x="222" y="14" width="70" height="12" fill="#3c3c3c"/>
    <rect x="402" y="14" width="70" height="12" fill="#3c3c3c"/>
  </svg>
  <div style="position:absolute;left:44px;top:188px;font-size:12px;color:var(--orange)">$250k FFF</div>
  <div style="position:absolute;left:226px;top:188px;font-size:12px;color:var(--orange)">Deal details</div>
  <div style="position:absolute;left:402px;top:188px;font-size:12px;color:var(--orange)">Planned raise</div>
</section>
<section class="slide" style="left:556px;top:2160px;width:512px;height:262px">
  <div class="bar"><span class="dot"></span>How to Fuel Growth</div>
  <svg style="position:absolute;left:0;top:0" width="512" height="262" aria-hidden="true">
    <rect x="170" y="70" width="62" height="46" rx="8" fill="#fff" stroke="#ccc"/>
    <rect x="288" y="70" width="62" height="46" rx="8" fill="#fff" stroke="#ccc"/>
    <rect x="170" y="160" width="62" height="46" rx="8" fill="#fff" stroke="#ccc"/>
    <rect x="288" y="160" width="62" height="46" rx="8" fill="#fff" stroke="#ccc"/>
    <circle cx="260" cy="138" r="44" fill="#4a4a4a"/>
    <circle cx="260" cy="138" r="14" fill="none" stroke="#fff" stroke-width="3"/>
  </svg>
  <div class="box-label" style="left:50px;top:74px;text-align:right;width:110px">Digital marketing<br>expertise</div>
  <div class="box-label" style="left:362px;top:82px">Ramp up UK sales</div>
  <div class="box-label" style="left:50px;top:166px;text-align:right;width:110px">Accelerate<br>digital campaign</div>
  <div class="box-label" style="left:362px;top:166px">Customer journey<br>management</div>
</section>

<!-- Row 9 -->
<section class="slide" style="left:6px;top:2455px;width:517px;height:292px">
  <div class="bar"><span class="dot"></span>How to Fuel Growth</div>
  <svg style="position:absolute;left:0;top:0" width="517" height="292" aria-hidden="true">
    <rect x="168" y="84" width="62" height="48" rx="8" fill="#f6a531"/>
    <rect x="288" y="84" width="62" height="48" rx="8" fill="#f6a531"/>
    <rect x="168" y="176" width="62" height="48" rx="8" fill="#f6a531"/>
    <rect x="288" y="176" width="62" height="48" rx="8" fill="#f6a531"/>
    <circle cx="259" cy="154" r="42" fill="#f6a531" stroke="#fff" stroke-width="4"/>
    <circle cx="259" cy="154" r="14" fill="none" stroke="#fff" stroke-width="3"/>
    <line x1="0" y1="285" x2="517" y2="285" stroke="#2b2b2b" stroke-width="1.5"/>
  </svg>
  <div class="box-label" style="left:50px;top:90px;text-align:right;width:110px">Digital marketing<br>expertise</div>
  <div class="box-label" style="left:362px;top:98px">Ramp up UK sales</div>
  <div class="box-label" style="left:50px;top:184px;text-align:right;width:110px">Accelerate<br>digital campaign</div>
  <div class="box-label" style="left:362px;top:184px">Customer journey<br>management</div>
</section>
<section class="slide" style="left:554px;top:2455px;width:514px;height:292px">
  <div class="photo" style="left:0;top:0;width:150px;height:292px;background:linear-gradient(160deg,#e9d9bd,#b88a55 50%,#5e4430)" role="img" aria-label="Photo of a globe lit by warm light"></div>
  <div style="position:absolute;left:260px;top:26px;font-size:20px;color:var(--ink)">Summary</div>
  <ul class="tick" style="position:absolute;left:178px;top:72px;width:300px">
    <li>A clear problem for a big market</li>
    <li>The right people and a great pipeline of talent</li>
    <li>Great technology foundation and technical skills</li>
    <li>Paying customers in multiple countries</li>
    <li>A clear opportunity for capital to create and drive the growth engine</li>
  </ul>
  <div style="position:absolute;right:14px;bottom:14px;width:18px;height:18px;border-radius:50%;border:2px solid var(--navy)"></div>
</section>

</body>
</html>
```